Computer repair services flyer

This flyer / leaflet is required to promote my local computer and laptop repair business. It will primarily be used for pinning to notice boards when I get access to shared accommodation but I will also use it in the future for posting through letterboxes in affluent areas.

Company branding, logo, services, pricing, contact details etc. can be found on my website at : www.brightmendlaptops.co.uk

The services I would predominantly like to promote on this flyer are :

Speeding up slow / old computers
Virus removal
Lost data recovered
Broken laptop screen replacements
Dead laptops fixed
We buy and recycle broken laptops for cash

Other features to highlight :

Friendly and experienced
We are local (Near to Cardiff city center)
Quick repair turnaround - most repairs within 24hours
Affordable / No VAT
Free diagnostics
No Fix = No fee
Free collection and delivery
We Guarantee our work

Calls to action and attention grabbing if possible. Offer 10% off. Free cooling fan clean.

Size of flyer = A5 (210 x 148mm or 8.3 x 5.8in) portrait, single sided colour.

Target Market(s)

18 to 60 years

Industry/Entity Type

Accommodation

Requirements
Must have
• 02920 413657

```html
<!DOCTYPE html>
<html lang="en">
<head>
<meta charset="utf-8">
<title>Bright Mend Laptops – Computer Repair Flyer</title>
<link href="https://fonts.googleapis.com/css2?family=Arimo:wght@400;700&family=Tinos:wght@700&display=swap" rel="stylesheet">
<style>
  :root {
    --orange: #f7931e;
    --orange-soft: #fbc58a;
    --peach: #fde3c4;
    --grey-band: #77777a;
    --grey-arc: #8a8a8d;
    --ink: #333333;
    --white: #ffffff;
    --navy: #1d2f8c;
    --navy-light: #6f8fe0;
    --bullet: #2d3d8f;
  }
  * { margin: 0; padding: 0; box-sizing: border-box; }
  html, body { width: 893px; height: 1200px; overflow: hidden; background: #ececec; }
  .flyer {
    position: relative;
    width: 893px; height: 1200px;
    background: var(--white);
    font-family: "Arimo", Arial, sans-serif;
    color: var(--ink);
    overflow: hidden;
  }
  .decor { position: absolute; inset: 0; }
  .top-band {
    position: absolute; left: 0; top: 0; width: 100%; height: 58px;
    background: var(--grey-band);
    color: var(--white);
    font-size: 29px; text-align: center; line-height: 58px;
    letter-spacing: 0.3px;
  }
  .hero-illustration {
    position: absolute; left: 35px; top: 76px; width: 125px; height: 100px;
    background: linear-gradient(160deg, #5b5b5e, #c9c9cc 60%, #e04b3a);
    border-radius: 6px;
  }
  .call-now {
    position: absolute; left: 164px; top: 172px;
    font-size: 36px; color: #111;
  }
  .phone-pill {
    position: absolute; left: 48px; top: 212px; width: 392px; height: 60px;
    background: var(--orange); border-radius: 14px;
    color: var(--white); font-size: 47px; text-align: center; line-height: 60px;
    letter-spacing: 1px;
  }
  .brand-name {
    position: absolute; left: 515px; top: 205px; width: 350px;
    font-size: 44px; font-weight: 700; color: var(--orange); line-height: 1.1;
  }
  .section-pill {
    position: absolute; height: 44px; border-radius: 12px;
    background: var(--orange); color: var(--white);
    font-size: 36px; line-height: 44px; padding-left: 30px;
  }
  .services-pill { left: 18px; top: 353px; width: 322px; }
  .features-pill { left: 326px; top: 629px; width: 350px; padding-left: 32px; }
  .list { position: absolute; list-style: none; font-size: 22px; line-height: 36px; }
  .list li { position: relative; padding-left: 20px; }
  .list li::before {
    content: ""; position: absolute; left: 0; top: 12px;
    width: 12px; height: 12px; border-radius: 50%;
    background: radial-gradient(circle at 35% 35%, #8fa2e8, var(--bullet) 70%);
  }
  .services-list { left: 38px; top: 408px; }
  .features-list { left: 342px; top: 685px; }
  .features-list .emph { font-weight: 700; font-size: 23px; }
  .offer-badge {
    position: absolute; left: 73px; top: 712px; width: 164px; height: 164px; border-radius: 50%;
    background: radial-gradient(circle at 40% 30%, var(--navy-light), var(--navy) 70%);
    color: var(--white); font-family: "Tinos", "Times New Roman", serif; font-weight: 700;
    font-size: 32px; line-height: 38px; text-align: center;
    display: flex; flex-direction: column; justify-content: center;
  }
  .bottom-band {
    position: absolute; left: 0; top: 1015px; width: 100%; height: 185px;
    background: var(--grey-band);
  }
  .laptop-photo {
    position: absolute; left: 10px; top: 930px; width: 305px; height: 262px;
    background: linear-gradient(150deg, #c9ced8, #6d8fc4 45%, #3a3c44 80%);
    border-radius: 6px;
  }
  .contact {
    position: absolute; left: 351px; top: 1027px;
    color: var(--white); font-size: 24px; line-height: 28.5px;
  }
  .fan-clean {
    position: absolute; left: 347px; top: 1146px;
    color: var(--orange); font-size: 35px; letter-spacing: 0.5px;
  }
</style>
</head>
<body>
<div class="flyer">
  <svg class="decor" width="893" height="1200" viewBox="0 0 893 1200" aria-hidden="true">
    <circle cx="760" cy="350" r="330" fill="var(--grey-arc)"/>
    <circle cx="740" cy="290" r="330" fill="var(--peach)"/>
    <circle cx="780" cy="250" r="270" fill="var(--orange-soft)" opacity="0.7"/>
    <circle cx="700" cy="260" r="230" fill="var(--white)"/>
    <circle cx="372" cy="300" r="38" fill="none" stroke="var(--orange-soft)" stroke-width="14" opacity="0.6"/>
    <path d="M893 740 L700 870 L893 860 Z" fill="#d6d6d8"/>
    <circle cx="800" cy="900" r="250" fill="var(--peach)" opacity="0.8"/>
    <circle cx="720" cy="960" r="200" fill="var(--white)" opacity="0.55"/>
  </svg>

  <div class="top-band">GREAT TECH SUPPORT IS ONLY A PHONE CALL AWAY</div>

  <div class="hero-illustration" role="img" aria-label="Laptop with a telephone handset cord wrapped around it"></div>
  <div class="call-now">Call Now</div>
  <div class="phone-pill">02920 413657</div>

  <div class="brand-name">Bright Mend Laptops</div>

  <div class="section-pill services-pill">Services</div>
  <ul class="list services-list">
    <li>Speeding up slow / old computers</li>
    <li>Virus removal</li>
    <li>Lost data recovered</li>
    <li>Broken laptop screen replacements</li>
    <li>Dead laptops fixed</li>
    <li>We buy and recycle broken laptops<br>for cash</li>
  </ul>

  <div class="section-pill features-pill">Other features</div>
  <ul class="list features-list">
    <li>Friendly and experienced</li>
    <li class="emph">We are local (Near to Cardiff city center)</li>
    <li>Quick repair turnaround - most repairs within<br>24 hours</li>
    <li>Affordable / No VAT</li>
    <li>Free diagnostics</li>
    <li>No Fix = No fee</li>
    <li>Free collection and delivery</li>
    <li>We Guarantee our work</li>
  </ul>

  <div class="offer-badge"><span>OFFER</span><span>10%</span><span>OFF</span></div>

  <div class="bottom-band"></div>
  <div class="laptop-photo" role="img" aria-label="Laptop with a cracked, shattered screen"></div>
  <div class="contact">
    14 Alder Grove Llanishen<br>
    Cardiff CF14 7QX<br>
    owen@brightmendlaptops.co.uk<br>
    www.brightmendlaptops.co.uk
  </div>
  <div class="fan-clean">FREE COOLING FAN CLEAN.</div>
</div>
</body>
</html>
```